Estrogen Wordpress Redesign Website

IMPORTANT: the design will need to look nice on mobile...so please keep that in mind!
We need to redesign our current Wordpress page to make it more appealing and look like an ecommerce page. We need the ability to implement this design on our Wordpress site.

Here is the current page:
https://www.kbtarvenhub.com/supplements/velunara/

However, the reference sample of what it has to look like or complement is also attached.

Attached is the Word document is the copy for the new page and the FAQs text.

The color palette has to match the reference sample attached.
Thanks!

Target Market(s)

women over 40

Requirements
Must have
• only use pics we provided in drobox; NO RANDOM stock photography

```html
<!DOCTYPE html>
<html lang="en">
<head>
<meta charset="utf-8">
<title>Menopause Support Bundle</title>
<link rel="stylesheet" href="https://fonts.googleapis.com/css2?family=Outfit:wght@500;600;700&family=Nunito+Sans:wght@400;600;700&display=swap">
<style>
:root{
  --ink:#1f2233;
  --text:#3a3d4d;
  --pink:#ec4b84;
  --magenta:#d45acb;
  --violet:#a35ee8;
  --card:#fdeff5;
  --card-blob:#fadbe8;
  --navy:#1d2438;
  --navy-deep:#161b2c;
  --muted:#8b8f9c;
  --footer-text:#d7d9e2;
}
*{box-sizing:border-box;margin:0;padding:0}
html,body{width:1200px;height:2620px;overflow:hidden;background:#fff}
body{position:relative;font-family:"Nunito Sans",sans-serif;color:var(--text)}
.abs{position:absolute}
h1,h2,h3,h4{font-family:"Outfit",sans-serif;color:var(--ink)}
.accent{background:linear-gradient(90deg,var(--pink),var(--violet));-webkit-background-clip:text;background-clip:text;color:transparent}

.section-title{left:13px;top:62px;font-size:29px;font-weight:600}
.section-title::after{content:"";position:absolute;left:0;right:0;bottom:-6px;height:3px;border-radius:2px;background:linear-gradient(90deg,var(--pink),var(--violet))}

.product-card{left:12px;width:1176px;height:340px;background:var(--card);border-radius:16px;box-shadow:0 4px 14px rgba(220,120,160,.08);overflow:hidden}
.blob{position:absolute;width:124px;height:124px;border-radius:50%;background:var(--card-blob);opacity:.7}
.blob.tr{right:-62px;top:-62px}
.blob.bl{left:-62px;bottom:-62px}
.badge{position:absolute;left:26px;top:25px;height:31px;padding:0 19px;border-radius:16px;color:#fff;font-weight:700;font-size:13px;line-height:31px;background:linear-gradient(90deg,var(--pink),#f05060);box-shadow:0 3px 8px rgba(236,75,132,.3)}
.badge.violet{background:linear-gradient(90deg,var(--pink),var(--violet))}
.badge.fade{background:linear-gradient(90deg,var(--pink),#fbd0e0 85%,#fff)}
.card-body{position:absolute;left:26px;width:740px}
.card-body h3{font-size:20px;font-weight:600;margin-bottom:14px}
.card-body p{font-size:14px;line-height:23px}
.product-shot{position:absolute;left:849px;width:230px;height:236px;border-radius:50%;background:radial-gradient(circle at 55% 45%,#ffffff 30%,#eef2f1 70%,#dfe8e5);box-shadow:0 6px 18px rgba(0,0,0,.08)}
.product-shot.ring{border:3px solid #dd8fd8}

.featured{left:12px;top:1288px;width:1176px;height:134px;border-radius:14px;background:linear-gradient(90deg,#fdf3f7,#f7f6fd);box-shadow:0 2px 10px rgba(0,0,0,.05)}
.featured-label{left:0;width:1200px;top:1327px;text-align:center;font-size:11px;font-weight:700;letter-spacing:.6px;color:var(--muted)}
.featured-strip{left:106px;top:1350px;width:976px;height:70px;background:#fff}
.featured-strip2{left:30px;top:1368px;width:1142px;height:60px;background:#fff}
.logo-row{left:110px;top:1398px;width:990px;display:flex;justify-content:space-between;align-items:center}
.logo-row span{display:block;height:34px;border-radius:6px;background:#c9cbd1}

.relief-title{left:0;width:1200px;top:1570px;text-align:center;font-size:29px;font-weight:600}
.symptoms{left:13px;top:1705px;font-family:"Outfit",sans-serif;font-size:20px;font-weight:600;line-height:26px;color:var(--pink)}
.relief-list{left:13px;top:1780px;width:790px;list-style:none}
.relief-list li{position:relative;padding-left:28px;font-size:14px;line-height:22px;margin-bottom:18px}
.relief-list li::before{content:"";position:absolute;left:0;top:3px;width:17px;height:17px;border-radius:50%;background:radial-gradient(circle,var(--pink) 0 2px,#e59bc8 3px)}
.portrait-halo{left:849px;top:1652px;width:290px;height:390px;border-radius:50%;background:#fde3ee}
.portrait{left:850px;top:1656px;width:284px;height:384px;border-radius:50%;border:3px solid #ee5f86;background:linear-gradient(180deg,#fbe0ea,#f2e6ee 55%,#e4e1e6)}

.footer-bg{left:0;top:2110px;width:1200px;height:510px}
.footer{left:0;top:2170px;width:1200px;height:450px;background:linear-gradient(180deg,var(--navy),var(--navy-deep))}
.brand{left:12px;top:2175px;font-family:"Outfit",sans-serif;font-size:24px;font-weight:700;color:#8a7db0;letter-spacing:1px}
.brand-copy{left:12px;top:2222px;width:270px;font-size:13px;line-height:19px;color:var(--footer-text)}
.socials{left:12px;top:2316px;display:flex;gap:12px}
.socials span{width:32px;height:32px;border-radius:50%;background:#2d3448;display:flex;align-items:center;justify-content:center}
.socials span i{width:11px;height:11px;border-radius:50%;background:#dfe1e8}
.col-title{top:2181px;font-size:16px;font-weight:600;color:#fff;font-family:"Outfit",sans-serif}
.col-title::after{content:"";position:absolute;left:0;bottom:-8px;width:38px;height:3px;border-radius:2px;background:linear-gradient(90deg,var(--pink),var(--violet))}
.links{top:2220px;list-style:none;font-size:13px;color:var(--footer-text)}
.links li{height:31.3px}
.contact{left:922px;list-style:none;font-size:13px;color:var(--footer-text)}
.contact li{position:absolute;left:0;display:flex;gap:8px;width:270px;line-height:18px}
.icon{flex:none;width:23px;height:23px;border-radius:50%;background:#2d3448;display:flex;align-items:center;justify-content:center}
.news-title{left:922px;top:2355px;font-size:16px;font-weight:600;color:#fff;font-family:"Outfit",sans-serif}
.news-copy{left:922px;top:2386px;font-size:11.5px;color:var(--footer-text)}
.news-input{left:922px;top:2417px;width:266px;height:36px;border-radius:6px;border:1px solid #444b5f;background:#232a3e;font-size:12.5px;color:#aeb2bf;padding:0 12px;line-height:34px}
.news-btn{left:922px;top:2463px;width:266px;height:34px;border-radius:6px;background:linear-gradient(90deg,#f46a7e,#c87ae8);color:#fff;font-size:12px;font-weight:700;text-align:center;line-height:34px}
.bubble{border-radius:50%;background:rgba(255,255,255,.05)}
.footer-rule{left:12px;top:2545px;width:1176px;height:1px;background:#2e3548}
.copyright{left:0;width:1200px;top:2566px;text-align:center;font-size:11px;color:#aeb2bf}
.disclaimer{left:0;width:1200px;top:2588px;text-align:center;font-size:10px;color:#9ca0ad}
</style>
</head>
<body>

<h2 class="abs section-title">What's Inside the <span class="accent">Bundle?</span></h2>

<article class="abs product-card" style="top:147px">
  <div class="blob tr"></div>
  <span class="badge">Hormone Power</span>
  <div class="card-body" style="top:135px">
    <h3>Targeted Hormonal Support</h3>
    <p>A targeted, comprehensive solution for menopausal symptoms and unbalanced hormones. Our unique combination of ingredients supports hormone balance, adrenal health, and fights the symptoms of perimenopause and menopause through improved estrogen metabolism, reduced inflammation, and balanced cortisol levels.</p>
  </div>
  <div class="product-shot" style="top:75px" role="img" aria-label="Product photo of a supplement bottle and a cream tube"></div>
</article>

<article class="abs product-card" style="top:521px">
  <div class="blob bl"></div>
  <span class="badge violet">Lumaveil</span>
  <div class="card-body" style="top:136px">
    <h3>Intense Hydration &amp; Menopausal Relief</h3>
    <p>Combines advanced moisturizing power with targeted nutritional support for skin affected by menopause. This triple-action formula does more than just hydrate—it helps restore skin's youthful appearance while supporting the body's natural hormone balance for healthier, more radiant skin.</p>
  </div>
  <div class="product-shot ring" style="top:75px" role="img" aria-label="Product photo of a supplement bottle and a cream tube"></div>
</article>

<article class="abs product-card" style="top:901px">
  <div class="blob tr"></div>
  <span class="badge fade">Serenova</span>
  <div class="card-body" style="top:148px">
    <h3>Progesterone Cream for Hormonal Balance</h3>
    <p>Bioidentical natural progesterone cream formulated to complement estrogen balance and support daily mood and overall well-being, while also reducing menopausal symptoms.</p>
  </div>
  <div class="product-shot" style="top:75px" role="img" aria-label="Product photo of a supplement bottle and a cream tube"></div>
</article>

<div class="abs featured"></div>
<div class="abs featured-label">AS FEATURED IN</div>
<div class="abs featured-strip2"></div>
<div class="abs featured-strip"></div>
<div class="abs logo-row" aria-label="Media features">
  <span style="width:90px"></span><span style="width:52px"></span><span style="width:48px"></span><span style="width:38px"></span>
  <span style="width:66px"></span><span style="width:80px"></span><span style="width:160px"></span><span style="width:60px"></span>
</div>

<h2 class="abs relief-title">Find Relief. Feel Like <span class="accent">Yourself Again.</span></h2>
<p class="abs symptoms">Hot Flashes. Night sweats. Mood swings.<br>Stubborn weight gain. Vaginal dryness.</p>
<ul class="abs relief-list">
  <li>If you're hot, irritable, and aren't sleeping, you're not alone.</li>
  <li>Sourced with research, innovation, and experience in menopause care, the Menopause Support Bundle offers a comprehensive approach to the many symptoms of menopause.</li>
  <li>Menopause is a natural transition, but that doesn't mean you have to continue to suffer. Our products are specifically formulated to address the impacts of declining estrogen levels.</li>
  <li>Together, our products reduce hot flashes, improve sleep, protect the skin, alleviate dry vaginal dryness, balance hormone levels, increase energy, improve mood, and help you feel like yourself again.</li>
</ul>
<div class="abs portrait-halo"></div>
<div class="abs portrait" role="img" aria-label="Photo of a smiling woman standing behind a row of supplement bottles"></div>

<svg class="abs footer-bg" width="1200" height="510" viewBox="0 0 1200 510" aria-hidden="true">
  <path d="M0 52 C 250 0, 420 -5, 640 12 S 1050 30, 1200 0 L1200 510 L0 510 Z" fill="#1d2438"/>
</svg>
<footer class="abs footer"></footer>
<div class="abs bubble" style="left:1106px;top:2180px;width:62px;height:62px"></div>
<div class="abs bubble" style="left:400px;top:2240px;width:38px;height:38px"></div>
<div class="abs bubble" style="left:62px;top:2445px;width:50px;height:50px"></div>

<div class="abs brand">KBTARVEN</div>
<p class="abs brand-copy">Dedicated to supporting women through every stage of menopause with science-backed, natural solutions for better health and wellbeing.</p>
<div class="abs socials" aria-label="Social links"><span><i></i></span><span><i></i></span><span><i></i></span><span><i></i></span></div>

<h4 class="abs col-title" style="left:316px">SHOP</h4>
<ul class="abs links" style="left:316px">
  <li>All Products</li><li>Bundles</li><li>Subscriptions</li><li>Gift Cards</li><li>New Arrivals</li><li>Best Sellers</li>
</ul>
<h4 class="abs col-title" style="left:619px">HELP</h4>
<ul class="abs links" style="left:619px">
  <li>FAQ</li><li>Shipping &amp; Returns</li><li>Track Your Order</li><li>Contact Us</li><li>Privacy Policy</li><li>Terms of Service</li>
</ul>
<h4 class="abs col-title" style="left:922px">CONTACT US</h4>
<ul class="abs contact" style="top:0">
  <li style="top:2218px"><span class="icon"><svg width="11" height="9" viewBox="0 0 11 9"><rect x=".5" y=".5" width="10" height="8" rx="1" fill="none" stroke="#ec4b84"/><path d="M.8 1 5.5 5 10.2 1" fill="none" stroke="#ec4b84"/></svg></span><span style="padding-top:3px">support@kbtarvenhub.com</span></li>
  <li style="top:2254px"><span class="icon"><svg width="11" height="11" viewBox="0 0 24 24"><path d="M6.6 10.8a15 15 0 0 0 6.6 6.6l2.2-2.2a1 1 0 0 1 1-.25 11.4 11.4 0 0 0 3.6.57 1 1 0 0 1 1 1V20a1 1 0 0 1-1 1A17 17 0 0 1 3 4a1 1 0 0 1 1-1h3.5a1 1 0 0 1 1 1c0 1.25.2 2.45.57 3.57a1 1 0 0 1-.25 1z" fill="#ec4b84"/></svg></span><span style="padding-top:3px">(800) 555-0199</span></li>
  <li style="top:2290px"><span class="icon" style="margin-top:8px"><svg width="10" height="12" viewBox="0 0 10 12"><path d="M5 11.5S1 7.2 1 4.6a4 4 0 0 1 8 0C9 7.2 5 11.5 5 11.5z" fill="none" stroke="#ec4b84"/><circle cx="5" cy="4.6" r="1.4" fill="none" stroke="#ec4b84"/></svg></span><span>48 Meadowlark Lane, Suite 210<br>Brightwater, OR 97301</span></li>
</ul>
<h4 class="abs news-title">Subscribe to our Newsletter</h4>
<p class="abs news-copy">Get exclusive offers, health tips, and product updates.</p>
<div class="abs news-input">Your email address</div>
<div class="abs news-btn">SUBSCRIBE</div>

<div class="abs footer-rule"></div>
<p class="abs copyright">© 2025 KBTARVEN. All rights reserved.</p>
<p class="abs disclaimer">*These statements have not been evaluated by the Food and Drug Administration. This product is not intended to diagnose, treat, cure, or prevent any disease.</p>

</body>
</html>
```